design a construction company business card

Design business card around our logo. Card must have all the typical info: name, title, address, phone, email, business name, etc. Somewhere on the card I would like to see our motto "Grounded in trust... Driven by dedication." Consider adding a splash of bright orange to the card to complement the blues and silvers/grays in the logo. We are open to metallic inks, textures, etc. We would like to see options on both light and dark backgrounds. The font in the logo is Euro Technic Extended Regular.

```html
<!DOCTYPE html>
<html lang="en">
<head>
<meta charset="utf-8">
<title>Halden Contracting – Business Card</title>
<link rel="stylesheet" href="https://fonts.googleapis.com/css2?family=Roboto:ital,wght@0,300;0,400;0,500;0,700;1,400&display=swap">
<style>
  :root {
    --page-bg: #e8e5e1;
    --card-white: #ffffff;
    --brand-blue: #25409a;
    --bright-blue: #1a6db8;
    --deep-blue: #233f97;
    --steel-gray: #808285;
    --text-gray: #58595b;
    --white: #ffffff;
  }
  * { box-sizing: border-box; margin: 0; padding: 0; }
  html, body {
    width: 1125px; height: 1200px; overflow: hidden;
    background: var(--page-bg);
    font-family: "Roboto", Arial, sans-serif;
  }
  .card {
    position: absolute; left: 171px; width: 826px; height: 472px;
    box-shadow: 0 3px 8px rgba(0,0,0,0.25);
    overflow: hidden;
  }
  .card--front { top: 106px; background: var(--card-white); }
  .card--back {
    top: 639px;
    background: radial-gradient(ellipse at 50% 40%, var(--bright-blue) 0%, #1d57a8 45%, var(--deep-blue) 100%);
    color: var(--white);
  }

  .wordmark { position: absolute; line-height: 1; }
  .wordmark__name { display: block; font-size: 62px; font-weight: 700; letter-spacing: 0.1em; }
  .wordmark__sub { display: block; font-size: 21px; font-weight: 400; margin-top: 2px; letter-spacing: 0.06em; }
  .card--front .wordmark { left: 57px; top: 147px; color: var(--brand-blue); }
  .card--back .wordmark { left: 0; right: 0; top: 244px; text-align: center; color: var(--white); }

  .person { position: absolute; left: 57px; top: 305px; }
  .person__name { font-size: 27px; font-weight: 700; color: var(--brand-blue); letter-spacing: 0.02em; }
  .person__title { font-size: 18px; font-weight: 300; color: var(--text-gray); margin-top: 6px; letter-spacing: 0.02em; }

  .contact { position: absolute; left: 529px; top: 266px; color: var(--text-gray); font-size: 18px; font-weight: 300; letter-spacing: 0.02em; }
  .contact__address { line-height: 25px; margin-bottom: 12px; }
  .contact__list { list-style: none; }
  .contact__item { display: flex; align-items: center; height: 26px; }
  .contact__icon { width: 16px; height: 16px; margin-right: 10px; fill: var(--brand-blue); flex: none; }

  .accent-bar { position: absolute; left: 0; bottom: 0; width: 100%; height: 17px; display: flex; }
  .accent-bar__gray { width: 347px; background: var(--steel-gray); }
  .accent-bar__gap { width: 3px; background: var(--white); }
  .accent-bar__blue { flex: 1; background: linear-gradient(90deg, var(--bright-blue), var(--deep-blue)); }

  .motto { position: absolute; left: 0; right: 0; top: 400px; text-align: center; font-size: 20px; font-style: italic; font-weight: 400; }
</style>
</head>
<body>
  <section class="card card--front">
    <div class="wordmark">
      <span class="wordmark__name">HALDEN</span>
      <span class="wordmark__sub">—CONTRACTING, INC.—</span>
    </div>
    <div class="person">
      <p class="person__name">MARK ELLISON</p>
      <p class="person__title">CEO/FOUNDER</p>
    </div>
    <div class="contact">
      <p class="contact__address">4120 Birchwood Drive<br>Fairbanks, Alaska 99701</p>
      <ul class="contact__list">
        <li class="contact__item">
          <svg class="contact__icon" viewBox="0 0 24 24" aria-hidden="true"><path d="M6.6 10.8a15.1 15.1 0 0 0 6.6 6.6l2.2-2.2a1 1 0 0 1 1-.25 11.4 11.4 0 0 0 3.6.57 1 1 0 0 1 1 1V20a1 1 0 0 1-1 1A17 17 0 0 1 3 4a1 1 0 0 1 1-1h3.5a1 1 0 0 1 1 1c0 1.250.2 2.450.57 3.57a1 1 0 0 1-.25 1z"/></svg>
          555 210 4873
        </li>
        <li class="contact__item">
          <svg class="contact__icon" viewBox="0 0 24 24" aria-hidden="true"><path d="M2 5h20v14H2zm2 2v.5l8 5 8-5V7zm0 2.8V17h16V9.8l-8 5z"/></svg>
          mark@haldenbuild.com
        </li>
        <li class="contact__item">
          <svg class="contact__icon" viewBox="0 0 24 24" aria-hidden="true"><circle cx="12" cy="12" r="10"/><path d="M7 8c2 0 3 1 3 2.5S8 13 9 15s2 1 2 3M14 4c0 2 2 2 3 3s0 3 2 3" stroke="#fff" stroke-width="1.6" fill="none"/></svg>
          www.haldenbuild.com
        </li>
      </ul>
    </div>
    <div class="accent-bar">
      <div class="accent-bar__gray"></div>
      <div class="accent-bar__gap"></div>
      <div class="accent-bar__blue"></div>
    </div>
  </section>

  <section class="card card--back">
    <div class="wordmark">
      <span class="wordmark__name">HALDEN</span>
      <span class="wordmark__sub">—CONTRACTING, INC.—</span>
    </div>
    <p class="motto">Grounded in trust... Driven by dedication.</p>
  </section>
</body>
</html>
```